Create a Brochure Design for Harlow Senior Living

Harlow Senior Living is a subsidiary of the Harlow Care Group. This brochure is specifically for the Harlow Senior Living company and brand. Create a 3 panel, front and back, tri-fold brochure. This brochure will be a way to introduce our senior living care home to the community, prospective, clients, and various referral partners. It is modern and state of the art home. Like the home, the brochure must be eye catching, unique in its deliverables (as it doesn’t feel like a care facility) and demonstrate both attention to detail and comfort. Our organization is sophisticated and built around warmth, care and individualized personal attention. The most important aspect of this design is to focus on creating a nurturing, warm, and inviting feel where you would want to put your own loved ones in our care home.
I am open to the creativity of the designer to develop something based on the above criteria; however I would like the design to work well with the existing collateral material. What I mean by that is that while I want everything to have its own personality and stand out as its own brand representative, I still need to be able to tell that the overall design concept stays stylistically inside of the same ‘family’ of existing designed material. Because of this, below I would like for the designer to pull inspiration from the link to our website (Located below) as well as from the attachment of our recently refreshed business cards (Attached). This should allow each design to be unique and creative, while still staying inside of a framework and the feel/style that I am looking for.
Finally, I want all the designers to understand that this brochure design is for a facility where we are responsible to provide care for active, positive, and happy seniors/elders. We have care professionals and staff on-site to provide 24x7, around the clock, care to the elders and geriatric residents as it is needed and required. The photos that are used must represent aging gracefully and with elegance.
Target Market(s)
Seniors(50+), Caring Family Members, Social Workers, Physicians, Hospitals
Industry/Entity Type
Business
Requirements
Must have
- • The company logo must be included.
Nice to have
- Attached you will find a sampling of images related to the long term care industry. Please feel free to use your own images as you see fit. The interior care home pictures are of our actual facility and should be incorporated into the brochure and your design.
Company Information
• Look under the Harlow Senior Living tab at
www.harlowcaregroup.example.

```html
<!DOCTYPE html>
<html lang="en">
<head>
<meta charset="utf-8">
<title>Harlow Senior Living – Tri-fold Brochure</title>
<link href="https://fonts.googleapis.com/css2?family=Crimson+Text:ital,wght@0,400;0,600;1,400;1,600&display=swap" rel="stylesheet">
<style>
  :root {
    --page-bg: #e9e9e9;
    --teal: #4f9997;
    --teal-dark: #3f8684;
    --teal-light: #7db7b4;
    --sand: #e4d8c7;
    --sand-light: #ece3d6;
    --sand-dark: #d2c3ae;
    --ink: #2a231e;
  }
  * { box-sizing: border-box; margin: 0; padding: 0; }
  html, body {
    width: 1200px; height: 931px; overflow: hidden;
    background: var(--page-bg);
    font-family: "Crimson Text", Georgia, serif;
    color: var(--ink);
  }
  .brochure {
    position: absolute; left: 100px; top: 80px;
    width: 1000px; height: 770px;
    background: var(--sand);
    box-shadow: 0 12px 30px rgba(0,0,0,0.18);
    overflow: hidden;
  }
  .brochure-art { position: absolute; inset: 0; }
  .photo { position: absolute; top: 34px; height: 226px; }
  .photo-bedroom { left: 0; width: 333px; background: linear-gradient(135deg, #c9b48a 0%, #8d6a45 45%, #d8c49c 100%); }
  .photo-lounge { left: 333px; width: 334px; background: linear-gradient(160deg, #e7dcc0 0%, #a48863 50%, #6f5a44 100%); }
  .photo-bathroom { left: 667px; width: 333px; background: linear-gradient(145deg, #f0ece4 0%, #d9cdb8 55%, #a57a4f 100%); }
  .panel { position: absolute; top: 0; width: 333px; height: 770px; }
  .panel-left { left: 0; }
  .panel-middle { left: 333px; }
  .panel-right { left: 667px; }
  .body-copy {
    position: absolute; top: 370px; left: 22px; right: 20px;
    font-size: 16.5px; line-height: 32px;
  }
  .panel-middle .body-copy { left: 20px; top: 366px; }
  .panel-right .body-copy { left: 20px; top: 368px; font-size: 16px; line-height: 31px; }
  .lead { font-style: italic; font-weight: 600; }
  .contact {
    position: absolute; left: 18px; top: 690px;
    font-size: 16.5px; line-height: 20px;
  }
  .tagline {
    position: absolute; left: 0; right: 0; top: 665px;
    text-align: center; font-size: 16.5px; line-height: 26px;
  }
  .brand {
    position: absolute; right: 22px; top: 668px;
    display: flex; flex-direction: column; align-items: center; gap: 8px;
    color: var(--teal-dark);
  }
  .brand-mark { width: 22px; height: 22px; background: var(--teal); }
  .brand-name { font-size: 20px; line-height: 22px; text-align: center; }
</style>
</head>
<body>
  <main class="brochure">
    <svg class="brochure-art" width="1000" height="770" viewBox="0 0 1000 770" aria-hidden="true">
      <rect width="1000" height="770" fill="var(--sand)"/>
      <rect x="333" y="0" width="334" height="770" fill="var(--sand-dark)" opacity="0.75"/>
      <path d="M0 560 C 250 520, 600 640, 1000 580 L1000 770 L0 770 Z" fill="var(--sand-light)" opacity="0.55"/>
      <path d="M0 640 C 300 600, 650 700, 1000 660 L1000 770 L0 770 Z" fill="var(--sand-light)" opacity="0.5"/>
      <path d="M0 0 L1000 0 L1000 40 C 700 20, 400 50, 0 30 Z" fill="var(--teal)"/>
      <path d="M0 250 L1000 250 L1000 365 C 850 320, 600 290, 333 290 C 180 290, 80 305, 0 330 Z" fill="var(--teal)"/>
      <path d="M0 250 L1000 250 L1000 300 C 700 270, 350 260, 0 285 Z" fill="var(--teal-light)" opacity="0.5"/>
      <line x1="333" y1="0" x2="333" y2="770" stroke="#000" stroke-opacity="0.06"/>
      <line x1="667" y1="0" x2="667" y2="770" stroke="#000" stroke-opacity="0.06"/>
    </svg>

    <div class="photo photo-bedroom" role="img" aria-label="Photo of a furnished private bedroom with sliding doors to a balcony"></div>
    <div class="photo photo-lounge" role="img" aria-label="Photo of the spacious shared living room with sectional sofa"></div>
    <div class="photo photo-bathroom" role="img" aria-label="Photo of an accessible tiled bathroom with grab bars and shower"></div>

    <section class="panel panel-left">
      <p class="body-copy"><span class="lead">The brand new, state of the art home</span> is located in Kailua at 48 Palm Terrace Drive in the Aikahi area. Up to 22 residents will enjoy 11,000 sq ft of living area with 19 private rooms with bathrooms (three can accommodate couples).</p>
      <p class="contact">For further information:<br>www.harlowhomecare.example</p>
    </section>

    <section class="panel panel-middle">
      <p class="body-copy">Each is fully furnished, including flat screen tv, electric bed, desk, chair, dressers, artwork, built-in closet system with mirrored doors, independent air conditioner, and ceiling fan.<br><span class="lead">Harlow Senior Living Kailua is truly a unique option for our kupuna.</span></p>
      <p class="tagline">Someone you can depend on...<br>Without question.</p>
    </section>

    <section class="panel panel-right">
      <p class="body-copy"><span class="lead">Based on a social model that encourages companionship, diversity, and the need to belong</span>, residents will enjoy a purposeful life with peace of mind. From basic lifestyle support to expanded personal care services, <span class="lead">staff is on-hand 24/7 to ensure each resident maximizes this dignified, loving, nurturing environment.</span></p>
      <div class="brand">
        <span class="brand-mark"></span>
        <span class="brand-name">Harlow<br>Senior Living</span>
      </div>
    </section>
  </main>
</body>
</html>
```